Dog themed post card for homeowners that may be willing to sell their house.

We will be sending these postcards to homeowners that may be interested in selling their house. Our business is themed around our dog "Biscuit"- Biscuit Gets Homes. We are using her as the focal point of the business because typically these homeowners get lots of mailers that are similar and we would like stand out with an inviting puppy dog.
We would like to included the icon for Chirpbook and Snapgrid with her handle "@BiscuitGetsHomes" and her website BiscuitGetsHomes-example.com and our phone number 555-482-1976.
We will be sending these postcards in batches to various subdivisions. For that reason please consider a format that can easily change the name of the subdivision. We are including the subdivision name because we want the postcard to be slightly more personal/targeted.
Our business is just starting and we would like to get some brand recognition going. We envision Biscuit Gets Homes predominately displayed somehow.
I have attached numerous pictures of Biscuit. We envision using one on each side of the postcard. Below are phrases we would like to include on the postcard in a format that you see fitting. Please use the verbiage below and not what is sketched on the uploaded postcard. The below verbiage is the most up to date.
-I recently bought a house in (subdivision name) and would love to buy yours.
-Call my humans today so we can give you a no obligation offer
-No money out of your pocket
-Quick closing
-Any condition
-Can help with moving expenses

Target Market(s)

Home owners with equity in their house that may need to sell quickly. These are generally people that do not enjoy the buying/selling of real estate. It can sometimes be someone who has recently inherited a home and doesnt want to deal with the headache. Other times it may be someone going through a divorce or forclosure and want to sell their home quickly.

Industry/Entity Type

Direct Marketing

Requirements
Must have
• Happy and bright feel. This industry is saturated with less than ethical people and we are trying to convey a very clean, honest, straight forward and scam-free process.

```html
<!DOCTYPE html>
<html lang="en">
<head>
<meta charset="utf-8">
<title>Biscuit Gets Homes – A6 Postcard</title>
<link rel="stylesheet" href="https://fonts.googleapis.com/css2?family=Oswald:wght@700&family=Open+Sans:ital,wght@0,400;0,700;1,400&family=Montserrat:wght@400;700&display=swap">
<style>
  :root {
    --sheet: #dedede;
    --pink: #e2007a;
    --ink: #111111;
    --white: #ffffff;
    --panel: rgba(70, 62, 56, 0.84);
    --label: #f4f4f4;
    --rule: #8a8a8a;
  }
  * { box-sizing: border-box; margin: 0; padding: 0; }
  html, body { width: 790px; height: 1200px; overflow: hidden; background: var(--sheet); }
  body { position: relative; font-family: "Open Sans", sans-serif; color: var(--white); }

  .card { position: absolute; left: 54px; width: 698px; height: 503px; overflow: hidden; }
  .card--front { top: 56px; }
  .card--back { top: 627px; background: var(--pink); }

  .side-label {
    position: absolute; left: 54px; font-family: "Montserrat", sans-serif;
    font-size: 17px; color: var(--label); letter-spacing: 0.5px;
  }
  .side-label--front { top: 574px; }
  .side-label--back { top: 1143px; }

  /* Wordmark: name set plainly in the body heading font, one weight, one colour */
  .wordmark {
    font-family: "Montserrat", sans-serif; font-weight: 700; color: var(--white);
    line-height: 1.05;
  }

  /* FRONT */
  .front-photo {
    position: absolute; inset: 0;
    background: linear-gradient(160deg, #cfcac3 0%, #b9b3ab 30%, #9a9f86 55%, #6f7a55 75%, #8a7357 100%);
  }
  .dog-cutout { position: absolute; left: 36px; top: 10px; width: 290px; height: 470px; }
  .dog-photo-area { fill: #c9c6c2; stroke: #111; stroke-width: 2.5; stroke-dasharray: 9 6; }
  .badge {
    position: absolute; left: 48px; top: 262px; width: 150px; height: 150px; border-radius: 50%;
    background: var(--pink); text-align: center; padding-top: 30px;
    font-family: "Montserrat", sans-serif; font-weight: 700; font-size: 17px; line-height: 1.05;
    transform: rotate(-14deg);
  }
  .badge__today {
    display: inline-block; margin-top: 4px; padding: 0 6px; background: var(--white); color: var(--ink);
    font-family: "Oswald", sans-serif; font-size: 27px; line-height: 1.1;
  }

  .front-panel {
    position: absolute; left: 288px; top: 43px; width: 376px; height: 407px;
    background: var(--panel); text-align: center; padding-top: 24px;
  }
  .front-panel .wordmark { font-size: 30px; }

  .headline {
    font-family: "Oswald", sans-serif; font-size: 31px; line-height: 1.1; text-transform: uppercase;
    margin-top: 22px;
  }
  .pitch { position: relative; font-size: 15px; line-height: 1.25; margin-top: 20px; padding: 0 26px; }
  .pitch__quote { position: absolute; font-family: Georgia, serif; font-size: 44px; font-weight: 700; line-height: 1; }
  .pitch__quote--open { left: 10px; top: -8px; }
  .pitch__quote--close { right: 10px; bottom: -24px; }
  .pitch__points { list-style: none; font-size: 15.5px; }
  .pitch__points li span::before { content: "• "; color: var(--pink); }

  /* BACK */
  .back-brand { position: absolute; left: 44px; top: 42px; }
  .back-brand .wordmark { font-size: 52px; }

  .dog-drawing {
    position: absolute; left: 32px; top: 187px; width: 145px; height: 156px;
    background: linear-gradient(180deg, #f2f2f2 0%, #bdbdbd 100%); border-radius: 60px 60px 10px 10px;
  }
  .questions {
    position: absolute; left: 188px; top: 168px; width: 225px; color: var(--ink);
    font-size: 15px; line-height: 1.2;
  }
  .questions ul { list-style: none; }
  .questions li { padding-left: 10px; text-indent: -10px; }
  .questions li::before { content: "• "; }
  .questions__cta { color: var(--white); font-weight: 700; font-size: 15.5px; margin-top: 2px; }
  .questions__aside { font-style: italic; font-size: 14.5px; }

  .contact-band {
    position: absolute; left: 0; right: 0; top: 343px; bottom: 0; background: var(--ink);
    padding: 10px 0 0 36px; font-family: "Montserrat", sans-serif; font-weight: 700;
  }
  .contact { display: flex; align-items: center; gap: 10px; }
  .contact__icon { width: 32px; height: 32px; flex: none; }
  .contact--phone { font-size: 38px; }
  .contact--phone .contact__icon { width: 38px; height: 38px; }
  .contact--web { font-size: 18px; margin-top: 8px; }
  .contact--social { font-size: 20px; margin-top: 8px; }
  .social-dot { width: 22px; height: 22px; border-radius: 50%; background: var(--pink); flex: none; }

  .coupon {
    position: absolute; left: 420px; top: 50px; width: 160px; height: 424px; z-index: 2;
    background: var(--white); border: 2px dashed #666; border-radius: 70px 70px 14px 14px;
    color: var(--ink); padding: 24px 10px 0 8px;
  }
  .coupon__lead { font-size: 13px; line-height: 1.2; text-align: center; padding: 0 8px; }
  .coupon__note { font-size: 8.5px; text-align: center; margin-top: 5px; }
  .coupon__field { display: flex; align-items: flex-end; font-size: 8px; margin-top: 9px; height: 20px; }
  .coupon__field label { width: 38px; text-align: right; padding-right: 5px; line-height: 1.1; flex: none; }
  .coupon__field span { flex: 1; border-bottom: 1.5px dashed var(--rule); height: 1px; }
  .coupon__line { border-bottom: 1.5px dashed var(--rule); margin: 16px 0 0 8px; }
  .coupon__send { position: relative; font-size: 8px; line-height: 1.25; margin-top: 18px; padding-left: 24px; text-align: center; }
  .coupon__pin { position: absolute; left: 2px; top: 0; }
</style>
</head>
<body>

<section class="card card--front">
  <div class="front-photo" role="img" aria-label="Photo of a house front yard with a path and shrubs, softly blurred"></div>
  <svg class="dog-cutout" viewBox="0 0 290 470" role="img" aria-label="Cut-out photo of Biscuit, a fluffy grey and white sheepdog wearing a striped bandana">
    <path class="dog-photo-area" d="M70 40 C90 5 180 5 200 40 C225 70 215 120 200 150 C240 190 270 260 265 340 C262 400 255 440 220 455 L40 455 C15 440 10 400 15 340 C20 260 40 190 70 150 C55 120 50 70 70 40 Z"/>
  </svg>
  <div class="badge">WE MAY<br>BUY YOUR<br>HOUSE...<br><span class="badge__today">Today!</span></div>

  <div class="front-panel">
    <p class="wordmark">Biscuit Gets Homes</p>
    <h1 class="headline">Take a short cut to<br>selling your home<br>in (area name)</h1>
    <div class="pitch">
      <span class="pitch__quote pitch__quote--open">‘</span>
      <p>My name is Biscuit and I'm a good dog. I recently bought a house in (area name) and would love to buy yours.<br>Call my human owners today so we can give you a no obligation offer.</p>
      <ul class="pitch__points">
        <li><span>No money out of your pocket</span></li>
        <li><span>Quick closing</span> <span>Any condition</span></li>
        <li><span>We can help with moving expenses</span></li>
      </ul>
      <span class="pitch__quote pitch__quote--close">’</span>
    </div>
  </div>
</section>
<p class="side-label side-label--front">FRONT OF A6 CARD</p>

<section class="card card--back">
  <div class="back-brand">
    <p class="wordmark">Biscuit<br>Gets Homes</p>
  </div>

  <div class="dog-drawing" role="img" aria-label="Black and white line illustration of Biscuit peeking over the edge"></div>

  <div class="questions">
    <ul>
      <li>Need to sell quickly?</li>
      <li>Need to avoid the pitfalls involved if selling an inherited house?</li>
      <li>Need a quick sale due to divorce or foreclosure?</li>
    </ul>
    <p class="questions__cta">You need to call Biscuit!</p>
    <p class="questions__aside">Need we say more?</p>
  </div>

  <div class="contact-band">
    <div class="contact contact--phone">
      <svg class="contact__icon" viewBox="0 0 38 38" aria-hidden="true">
        <circle cx="19" cy="19" r="19" fill="#e2007a"/>
        <path d="M13 10 l4 0 2 6 -3 2 c1 3 3 5 6 6 l2 -3 6 2 0 4 c-10 1 -18 -7 -17 -17z" fill="#fff"/>
      </svg>
      <span>555-482-1976</span>
    </div>
    <div class="contact contact--web">
      <svg class="contact__icon" viewBox="0 0 32 32" aria-hidden="true">
        <circle cx="16" cy="16" r="16" fill="#e2007a"/>
        <circle cx="16" cy="16" r="9" fill="none" stroke="#fff" stroke-width="2"/>
        <path d="M7 16 h18 M16 7 c-5 6 -5 12 0 18 M16 7 c5 6 5 12 0 18" fill="none" stroke="#fff" stroke-width="1.6"/>
      </svg>
      <span>BiscuitGetsHomes-example.com</span>
    </div>
    <div class="contact contact--social">
      <span class="social-dot" aria-label="Chirpbook"></span>
      <span class="social-dot" aria-label="Snapgrid"></span>
      <span>@BiscuitGetsHomes</span>
    </div>
  </div>

  <div class="coupon">
    <p class="coupon__lead">Call us or clip and send this coupon and find out more about our pedigree house buying service</p>
    <p class="coupon__note">Please contact me to make an offer</p>
    <div class="coupon__field"><label>Your Name:</label><span></span></div>
    <div class="coupon__field"><label>Your Address:</label><span></span></div>
    <div class="coupon__line"></div>
    <div class="coupon__line"></div>
    <div class="coupon__field"><label>Your tel no:</label><span></span></div>
    <div class="coupon__field"><label>Best time to call:</label><span></span></div>
    <div class="coupon__field"><label>Your email:</label><span></span></div>
    <p class="coupon__send">
      <svg class="coupon__pin" width="18" height="22" viewBox="0 0 20 24" aria-hidden="true">
        <path d="M10 0 a9 9 0 0 1 9 9 c0 7 -9 15 -9 15 s-9 -8 -9 -15 a9 9 0 0 1 9 -9z" fill="#e2007a"/>
        <circle cx="10" cy="9" r="3.5" fill="#fff"/>
      </svg>
      Send to: Biscuit Gets Homes, Any Street, Any Town, Any County, ZIP CODE
    </p>
  </div>
</section>
<p class="side-label side-label--back">BACK OF A6 CARD</p>

</body>
</html>
```